Power Point make-over

We need an immediate turn around on this power point project. The presentation needs a make-over. The project includes:
1. Creating uniformity in font, colors, etc.
2. Enhancing charts and graphs.
3. Producing a better layout.
4. Some sildes can be combines.
5. The "notes" on certain slides should appear on the slide.
6. Add Harbor Lantern Consulting logo- maybe as footer.

Finally- Each section (Weave the Years- Quill Sorters- KRW exercise) of the power point is used in the same presentation so it needs uniformity but it does not require a segway. These exercises are also used individually for shorter presentations, so I need them to be able to stand alone. Ultimately, I need to be able to edit the power point as needed.

Target Market(s)

CEO, Executives

Industry/Entity Type

Consulting

Requirements
Must have
• The project includes:

Nice to have
• I prefer a plain white background.

```html
<!DOCTYPE html>
<html lang="en">
<head>
<meta charset="utf-8">
<title>Weave the Years – Slides</title>
<link rel="stylesheet" href="https://fonts.googleapis.com/css2?family=Source+Sans+3:wght@400;600;700&family=Caveat:wght@400&display=swap">
<style>
  :root {
    --green: #006b4f;
    --green-soft: #c7d4cb;
    --green-mid: #a9bcae;
    --ink: #1f1f1f;
    --grey: #6b6b6b;
    --grid: #dcdcdc;
    --page: #ffffff;
    --slide-edge: #e6e6e6;
  }
  * { box-sizing: border-box; margin: 0; padding: 0; }
  html, body { width: 1200px; height: 1000px; overflow: hidden; background: var(--page); }
  body { position: relative; font-family: "Source Sans 3", Arial, sans-serif; color: var(--ink); }

  .slide {
    position: absolute; left: 283px; width: 568px; height: 436px;
    background: var(--page); border: 1px solid var(--slide-edge); overflow: hidden;
  }
  .slide--intro { top: 34px; }
  .slide--chart { top: 519px; }

  .title-bar {
    position: absolute; left: 43px; top: 46px; width: 264px; height: 44px;
    border-radius: 22px 0 0 22px;
    background: linear-gradient(90deg, var(--green) 0%, var(--green) 55%, rgba(0,107,79,0) 100%);
    display: flex; align-items: center;
  }
  .title-bar__dot {
    width: 40px; height: 40px; margin-left: 2px; border-radius: 50%;
    background: var(--page); border: 3px solid var(--grey);
  }
  .title-bar__text { margin-left: 12px; color: #fff; font-weight: 700; font-size: 22px; letter-spacing: -0.2px; white-space: nowrap; }

  .points { position: absolute; left: 79px; top: 120px; width: 420px; list-style: none; }
  .points li { position: relative; padding-left: 19px; font-size: 12.4px; line-height: 15.6px; margin-bottom: 14px; }
  .points li::before {
    content: ""; position: absolute; left: 0; top: 2px; width: 11px; height: 11px;
    border-radius: 50%; border: 2px solid var(--grey); background: var(--page);
  }
  .points strong { color: var(--green); font-weight: 700; }

  .footer-brand {
    position: absolute; left: 57px; bottom: 20px; display: flex; align-items: center; gap: 5px;
  }
  .footer-brand__dot { width: 30px; height: 30px; border-radius: 50%; border: 3px solid var(--grey); flex: none; }
  .footer-brand__name { color: var(--green); font-weight: 700; font-size: 10.5px; line-height: 11px; white-space: nowrap; }
  .footer-brand__name span { display: block; font-size: 6.5px; letter-spacing: 2.2px; font-weight: 700; color: var(--green); }

  .tagline-band {
    position: absolute; left: 193px; right: 0; bottom: 12px; height: 53px;
    background: var(--green); border-radius: 26px 0 0 26px;
    display: flex; align-items: center; padding-left: 38px;
  }
  .tagline-band__text { color: #fff; font-family: "Caveat", cursive; font-size: 21px; line-height: 1; white-space: nowrap; }

  .life-chart { position: absolute; left: 0; top: 0; }
  .life-chart text { font-family: "Source Sans 3", Arial, sans-serif; }
  .axis-label { font-size: 6px; font-weight: 700; fill: var(--ink); }
  .area-label { font-size: 5.5px; font-weight: 700; fill: var(--ink); }
</style>
</head>
<body>

<section class="slide slide--intro">
  <div class="title-bar"><div class="title-bar__dot"></div><h1 class="title-bar__text">Weave the Years</h1></div>
  <ul class="points">
    <li><strong>Purpose of this exercise:</strong> To offer a snap shot, yet detailed, view of life. It’s intended to help identify challenges and successes. When used month over month it can also offer insight into more specific behavior patterns</li>
    <li>This exercise can be completed for an individual assessment or for a group assessment. When used as a group, each person plots their own life, then each individual plots their findings on a “<strong>master graph</strong>”. This gives insight to commonalities and differences in a group.</li>
    <li>This is a great exercise when forums are having trouble with finding presentation topics, or when a forum wants to be a bit more introspective.</li>
  </ul>
  <div class="footer-brand"><div class="footer-brand__dot"></div><div class="footer-brand__name">HARBOR LANTERN<span>CONSULTING</span></div></div>
  <div class="tagline-band"><p class="tagline-band__text">A company specializing in changing behaviors</p></div>
</section>

<section class="slide slide--chart">
  <div class="title-bar"><div class="title-bar__dot"></div><h1 class="title-bar__text">Weave the Years</h1></div>

  <svg class="life-chart" width="568" height="436" viewBox="0 0 568 436">
    <g stroke="var(--grid)" stroke-width="0.8">
      <line x1="98" y1="138" x2="497" y2="138"/><line x1="98" y1="157" x2="497" y2="157"/>
      <line x1="98" y1="176" x2="497" y2="176"/><line x1="98" y1="194" x2="497" y2="194"/>
      <line x1="98" y1="213" x2="497" y2="213"/><line x1="98" y1="232" x2="497" y2="232"/>
      <line x1="98" y1="251" x2="497" y2="251"/>
      <line x1="131" y1="138" x2="131" y2="270"/><line x1="164" y1="138" x2="164" y2="270"/>
      <line x1="198" y1="138" x2="198" y2="270"/><line x1="231" y1="138" x2="231" y2="270"/>
      <line x1="264" y1="138" x2="264" y2="270"/><line x1="297" y1="138" x2="297" y2="270"/>
      <line x1="331" y1="138" x2="331" y2="270"/><line x1="364" y1="138" x2="364" y2="270"/>
      <line x1="397" y1="138" x2="397" y2="270"/><line x1="430" y1="138" x2="430" y2="270"/>
      <line x1="464" y1="138" x2="464" y2="270"/><line x1="497" y1="138" x2="497" y2="270"/>
    </g>
    <g stroke="var(--ink)" stroke-width="1.6">
      <line x1="98" y1="136" x2="98" y2="271"/><line x1="97" y1="270" x2="497" y2="270"/>
    </g>
    <g class="axis-label" text-anchor="end">
      <text x="90" y="149">70</text><text x="90" y="167">60</text><text x="90" y="185">50</text>
      <text x="90" y="203">40</text><text x="90" y="222">30</text><text x="90" y="240">20</text>
      <text x="90" y="258">10</text><text x="90" y="273">0</text>
    </g>
    <circle cx="514" cy="146" r="9" fill="var(--page)" stroke="var(--grey)" stroke-width="2.5"/>
    <circle cx="66" cy="271" r="9" fill="var(--page)" stroke="var(--grey)" stroke-width="2.5"/>

    <g>
      <polygon points="98,272 131,272 81,323 48,323" fill="var(--green-soft)"/>
      <polygon points="131,272 164,272 114,323 81,323" fill="var(--green-mid)"/>
      <polygon points="164,272 198,272 148,323 114,323" fill="var(--green-soft)"/>
      <polygon points="198,272 231,272 181,323 148,323" fill="var(--green-mid)"/>
      <polygon points="231,272 264,272 214,323 181,323" fill="var(--green-soft)"/>
      <polygon points="264,272 297,272 247,323 214,323" fill="var(--green-mid)"/>
      <polygon points="297,272 331,272 281,323 247,323" fill="var(--green-soft)"/>
      <polygon points="331,272 364,272 314,323 281,323" fill="var(--green-mid)"/>
      <polygon points="364,272 397,272 347,323 314,323" fill="var(--green-soft)"/>
      <polygon points="397,272 430,272 380,323 347,323" fill="var(--green-mid)"/>
      <polygon points="430,272 464,272 414,323 380,323" fill="var(--green-soft)"/>
      <polygon points="464,272 497,272 447,323 414,323" fill="var(--green-mid)"/>
    </g>
    <g class="area-label" text-anchor="middle">
      <text transform="translate(90,298) rotate(-48)">Marriage</text>
      <text transform="translate(123,292) rotate(-48)">Parenting</text>
      <text transform="translate(156,297) rotate(-48)">Work / Career</text>
      <text transform="translate(189,292) rotate(-48)">Social Life</text>
      <text transform="translate(222,296) rotate(-48)">Spiritual Life</text>
      <text transform="translate(256,297) rotate(-48)">Personal Health</text>
      <text transform="translate(289,292) rotate(-48)">Forum</text>
      <text transform="translate(322,292) rotate(-48)">Finance</text>
      <text transform="translate(355,292) rotate(-48)">Joy / Fun</text>
      <text transform="translate(388,289) rotate(-48)">Self</text>
      <text transform="translate(421,293) rotate(-48)">Hobbies</text>
      <text transform="translate(455,295) rotate(-48)">Friendships</text>
    </g>
  </svg>

  <div class="footer-brand"><div class="footer-brand__dot"></div><div class="footer-brand__name">HARBOR LANTERN<span>CONSULTING</span></div></div>
  <div class="tagline-band"><p class="tagline-band__text">A company specializing in changing behaviors</p></div>
</section>

</body>
</html>
```